"Breakthrough! Mapping the Coastal Escape" NEEDS BOOK COVER!

Hello - please see the attached BOOK COVER DESIGN BRIEF document for full instructions and content required for cover.

I am really seeking clean, professional designs here that follow my instructions. The cover MUST jump out in a thumbnail (as if on Brindlow) - any covers that are too busy, messy or unprofessional will be eliminated.

Any questions please ask.

Thanks.
Colin
Updates

Project Deadline Extended
Reason: This project has been extended to invite more designers, as I haven't received enough options to choose from. Hoping this extra few days allows a few more submissions. Thank you to existing designers for your submissions, a number of them are in the running.

Target Market(s)

Please see the attached brief for full instructions on this project.

Industry/Entity Type

Property

Font styles to use
Serif
Sans Serif

Requirements
Must have
• Please see the attached brief for full instructions on this project.
Nice to have
Should not have

```html
<!DOCTYPE html>
<html lang="en">
<head>
<meta charset="utf-8">
<title>Breakthrough! Mapping the Coastal Escape — Book Cover Spread</title>
<link rel="stylesheet" href="https://fonts.googleapis.com/css2?family=Archivo+Black&family=Libre+Baskerville:wght@400;700&family=Roboto+Condensed:ital,wght@0,400;0,700;1,400&display=swap">
<style>
  :root {
    --page-bg: #ececec;
    --back-blue: #55c8f2;
    --front-top: #58c9f1;
    --front-bottom: #a9dcf6;
    --spine-blue: #1f5cae;
    --pale-box: #a6dcf5;
    --skyline: #8fd6f5;
    --wave: #4fb6e4;
    --stamp-red: #e0262a;
    --banner-red: #e2231a;
    --ink: #141414;
    --ink-soft: #222831;
    --white: #ffffff;
    --sculpture: #8e9aa3;
    --photo-warm: #d9a47e;
    --photo-cool: #b9b4ae;
  }
  * { box-sizing: border-box; margin: 0; padding: 0; }
  html, body { width: 1200px; height: 1200px; overflow: hidden; }
  body { background: var(--page-bg); position: relative; font-family: "Roboto Condensed", Arial, sans-serif; }

  .spread {
    position: absolute; left: 48px; top: 219px; width: 1104px; height: 762px;
    box-shadow: 0 6px 14px rgba(0,0,0,.25);
  }

  /* Back cover */
  .back-cover { position: absolute; left: 0; top: 0; width: 536px; height: 762px; background: var(--back-blue); overflow: hidden; color: var(--ink-soft); }
  .testimonials { position: absolute; left: 30px; top: 54px; width: 492px; display: flex; gap: 20px; }
  .testimonial { flex: 1; position: relative; padding-left: 12px; font-size: 9.8px; line-height: 1.42; letter-spacing: -0.1px; }
  .testimonial::before { content: "\201C"; position: absolute; left: -4px; top: -10px; font-size: 28px; font-style: italic; color: var(--ink); }
  .testimonial .close { font-size: 24px; font-style: italic; line-height: 0; vertical-align: -9px; margin-left: 6px; }
  .testimonial cite { display: block; font-style: normal; font-weight: 700; margin-top: 1px; }

  .banner { position: absolute; left: 30px; top: 173px; width: 478px; height: 22px; background: var(--banner-red); color: var(--white); font-weight: 700; font-size: 13.4px; line-height: 22px; text-align: center; }
  .blurb { position: absolute; left: 30px; top: 200px; width: 490px; font-size: 9.8px; line-height: 1.42; letter-spacing: -0.1px; }
  .blurb .lead { font-size: 11.6px; font-weight: 700; line-height: 1.32; margin-bottom: 3px; letter-spacing: 0; }
  .blurb ul { list-style: none; margin-bottom: 2px; }
  .blurb li { position: relative; padding-left: 16px; margin-bottom: 1px; }
  .blurb li::before { content: ""; position: absolute; left: 2px; top: 4px; width: 6px; height: 6px; border-radius: 50%; background: var(--ink); }
  .blurb p { margin-bottom: 2px; }

  .author-box { position: absolute; left: 30px; width: 478px; background: var(--pale-box); display: flex; gap: 10px; padding: 7px 10px; font-size: 9.8px; line-height: 1.42; letter-spacing: -0.1px; }
  .author-box.helena { top: 417px; height: 110px; }
  .author-box.martin { top: 535px; height: 104px; }
  .author-photo { flex: 0 0 88px; height: 92px; }
  .helena .author-photo { background: linear-gradient(160deg, var(--photo-warm), #f3dccb); }
  .martin .author-photo { background: linear-gradient(160deg, var(--photo-cool), #e9e4de); }

  .back-skyline { position: absolute; left: 0; bottom: 0; width: 536px; height: 130px; }
  .brand-mark { position: absolute; left: 94px; top: 661px; width: 112px; height: 44px; background: var(--white); border: 1px solid var(--spine-blue); display: flex; align-items: center; justify-content: center; gap: 4px; font-size: 11px; font-weight: 700; color: var(--spine-blue); white-space: nowrap; }
  .brand-mark .dot { width: 8px; height: 8px; background: var(--spine-blue); }
  .website { position: absolute; left: 96px; top: 722px; font-size: 12.5px; font-weight: 700; color: var(--ink); }

  /* Spine */
  .spine { position: absolute; left: 536px; top: 0; width: 30px; height: 762px; background: var(--spine-blue); color: var(--white); }
  .spine-brand { position: absolute; left: 6px; top: 14px; width: 18px; height: 44px; border: 1px solid var(--white); writing-mode: vertical-rl; font-size: 8px; font-weight: 700; text-align: center; line-height: 16px; }
  .spine-authors { position: absolute; left: 3px; top: 68px; writing-mode: vertical-rl; font-family: "Libre Baskerville", Georgia, serif; font-size: 9px; line-height: 12px; }
  .spine-title { position: absolute; left: 7px; top: 168px; writing-mode: vertical-rl; font-family: "Archivo Black", Arial, sans-serif; font-size: 14px; letter-spacing: .3px; white-space: nowrap; }

  /* Front cover */
  .front-cover { position: absolute; left: 566px; top: 0; width: 538px; height: 762px; background: linear-gradient(180deg, var(--front-top) 0%, var(--front-top) 30%, var(--front-bottom) 62%); overflow: hidden; }
  .front-authors { position: absolute; top: 52px; width: 100%; text-align: center; font-family: "Libre Baskerville", Georgia, serif; font-weight: 700; font-size: 18px; color: var(--ink-soft); }
  .front-skyline { position: absolute; left: 0; top: 100px; width: 538px; height: 140px; }
  .stamp { position: absolute; left: 52px; top: 272px; padding: 0 14px; border: 6px solid var(--stamp-red); transform: rotate(-7deg); font-family: "Archivo Black", Arial, sans-serif; font-size: 52px; line-height: 78px; color: var(--stamp-red); }
  .title-main { position: absolute; right: 36px; top: 408px; font-family: "Archivo Black", Arial, sans-serif; font-size: 62px; line-height: 1; color: var(--ink); letter-spacing: -1px; }
  .title-sub { position: absolute; right: 36px; top: 478px; font-family: "Archivo Black", Arial, sans-serif; font-size: 25px; line-height: 1; color: var(--ink); }
  .tagline { position: absolute; right: 36px; top: 520px; width: 400px; text-align: center; font-family: "Libre Baskerville", Georgia, serif; font-weight: 700; font-size: 17px; line-height: 1.3; color: var(--ink-soft); }
  .sculpture { position: absolute; left: 296px; top: 600px; width: 150px; height: 150px; }
  .wave { position: absolute; left: 0; bottom: 0; width: 538px; height: 70px; }
</style>
</head>
<body>
<main class="spread">

  <section class="back-cover">
    <div class="testimonials">
      <blockquote class="testimonial">Martin professionally guided me through the process of applying for my first home loan. He made what would normally be a worrying task into something enjoyable and stress-free. I found Martin's knowledge and confidence in the home loan market impressive. Thank you for helping me make my first big step into a positive future.<span class="close">&#8221;</span>
        <cite>Peter Lang, QLD</cite></blockquote>
      <blockquote class="testimonial">I can't thank you enough for looking after us for over 10 years now and 5 loans later. No such thing as too hard basket for Martin, he will find a way to get you what you need. Professional, honest and reliable, with great product knowledge – and so friendly. An asset to have on your side when investing or buying your first home!<span class="close">&#8221;</span>
        <cite>Kim Ardley, QLD</cite></blockquote>
    </div>

    <div class="banner">Everything You Didn't Know About Property And Mortgages, But Wish You Did!</div>

    <div class="blurb">
      <p class="lead">Breakthrough! Mapping the Coastal Escape is the smart home buyers guide to mortgages, property, investing and making your dreams reality. This easy to read book will teach you:</p>
      <ul>
        <li><b>Five things you must know before buying a property and mortgage</b> – don't approach any bank or broker before understanding this.</li>
        <li><b>How to maximise your chances of getting your loan approved</b> – including help on deposit savings and working out how much you can borrow.</li>
        <li><b>The mortgage and property process explained in six easy steps</b> – with the five stressful mortgage mistakes to avoid.</li>
        <li><b>Tips to getting smarter with your money</b> – and how to pay off your home loan in record time.</li>
        <li><b>The accidental investor vs. the planned investor</b> – and why most Australians invest for the wrong reasons.</li>
      </ul>
      <p>The Great Australian Dream of owning your own property, or starting an investment portfolio, can become a great Australian nightmare if you don't have the right knowledge and team to support you and your dreams.</p>
      <p>So before taking your next step, read this book carefully and get the insider tips to make confident decisions with your money and your future.</p>
    </div>

    <div class="author-box helena">
      <div class="author-photo" role="img" aria-label="Portrait photograph of author Helena Varga"></div>
      <p><b>Helena Varga</b> bought her first investment property in 1995 and has never looked back. As Managing Director of Keystone Finance Cairns, she ensures all clients receive the highest level of personal service every step of the way, and enjoys helping people achieve their dream of getting into their own home or start investing. With three generations of one family as clients, Helena is driven to share her experiences in property and mortgages – so you too can learn the easy way and avoid costly mistakes with your money.</p>
    </div>

    <div class="author-box martin">
      <div class="author-photo" role="img" aria-label="Portrait photograph of author Martin Keller"></div>
      <p><b>Martin Keller</b> is an award winning mortgage broker with Keystone Finance Cairns. With over 40 years' experience in the finance world, he's worked in virtually every area of banking and lending in over a dozen different locations throughout Queensland. Along the way he's helped thousands of Australians secure finance for their dream home or investment property. No matter how simple or complex the challenge, with a world of insider knowledge and experience at his fingertips, you definitely want Martin to be on your finance team.</p>
    </div>

    <div class="back-skyline" role="img" aria-label="Pale outline illustration of a town skyline with houses and trees" style="background: linear-gradient(180deg, rgba(143,214,245,0) 0%, var(--skyline) 60%);"></div>
    <div class="brand-mark"><span class="dot"></span>Keystone Finance</div>
    <div class="website">www.keystonefinancecairns.au</div>
  </section>

  <section class="spine">
    <div class="spine-brand">Keystone</div>
    <div class="spine-authors">Martin Keller<br>Helena Varga</div>
    <div class="spine-title">BREAKTHROUGH! MAPPING the COASTAL ESCAPE</div>
  </section>

  <section class="front-cover">
    <div class="front-authors">Martin Keller &amp; Helena Varga</div>
    <div class="front-skyline" role="img" aria-label="White outline illustration of a city skyline with houses, towers and trees" style="background: linear-gradient(180deg, rgba(255,255,255,0) 0%, rgba(255,255,255,.18) 35%, rgba(143,214,245,.7) 100%);"></div>
    <div class="stamp">Breakthrough!</div>
    <h1 class="title-main">MAPPING</h1>
    <div class="title-sub">THE COASTAL ESCAPE</div>
    <p class="tagline">The Smart Home Buyers Guide To Mortgages, Property, Investing And Making Your Dreams Reality</p>
    <svg class="wave" viewBox="0 0 538 70" aria-hidden="true">
      <path d="M0 30 C60 10 110 44 180 30 S300 12 360 28 S470 40 538 22 V70 H0 Z" fill="var(--wave)"/>
      <path d="M0 30 C60 10 110 44 180 30 S300 12 360 28 S470 40 538 22" fill="none" stroke="var(--white)" stroke-width="2"/>
    </svg>
    <div class="sculpture" role="img" aria-label="Photograph of a metal fish sculpture on poles" style="background: radial-gradient(ellipse at 50% 40%, var(--sculpture) 0%, rgba(142,154,163,.5) 45%, rgba(142,154,163,0) 72%);"></div>
  </section>

</main>
</body>
</html>
```